Business Card Design Project

We need a business card design for our IT Managed Services firm.
Our logo is attached.
More information on our company can be found at:
www.dulvarosys.com
Target Market(s)
CEO, President. Mid Size Businesses
Industry/Entity Type
Business

```html
<!DOCTYPE html>
<html lang="en">
<head>
<meta charset="utf-8">
<title>Dulvaro Systems – Business Card Colourways</title>
<link rel="stylesheet" href="https://fonts.googleapis.com/css2?family=Arimo:wght@400;700&display=swap">
<style>
  :root {
    --page: #ffffff;
    --ink: #000000;
    --on-tab: #ffffff;
    --alert: #ff0000;

    --grey-light: #e8e8e8;
    --grey-mid: #cfcfcf;
    --tab-grey: #4d4d4d;

    --cyan-bright: #22ffff;
    --cyan-pale: #a8ffff;
    --cyan-deep: #00ccff;
    --tab-red: #ff0000;

    --aqua: #99ffff;
    --tab-sky: #00ccff;

    --lime: #ccff66;
    --tab-green: #99ff00;
  }

  * { margin: 0; padding: 0; box-sizing: border-box; }

  html, body {
    width: 1200px;
    height: 702px;
    overflow: hidden;
    background: var(--page);
    font-family: "Arimo", Arial, sans-serif;
  }

  .sheet {
    position: relative;
    width: 1200px;
    height: 702px;
  }

  .card {
    position: absolute;
    width: 578px;
    height: 329px;
    overflow: hidden;
  }
  .card--graphite { left: 5px;   top: 0;     background: radial-gradient(ellipse at 42% 48%, var(--grey-light) 0%, var(--grey-mid) 75%); }
  .card--ice      { left: 614px; top: 0;     background: linear-gradient(90deg, var(--cyan-bright) 0%, var(--cyan-bright) 25%, var(--cyan-pale) 48%, var(--cyan-deep) 100%); }
  .card--aqua     { left: 5px;   top: 368px; background: var(--aqua); }
  .card--lime     { left: 615px; top: 368px; background: var(--lime); }

  .name-tab {
    position: absolute;
    left: 0;
    top: 67px;
    width: 277px;
    height: 69px;
    border-radius: 0 10px 16px 0;
    box-shadow: 3px 4px 2px rgba(0, 0, 0, 0.8);
    color: var(--on-tab);
  }
  .card--graphite .name-tab { background: var(--tab-grey); }
  .card--ice .name-tab      { background: var(--tab-red); }
  .card--aqua .name-tab     { background: var(--tab-sky); }
  .card--lime .name-tab     { background: var(--tab-green); }

  .name-tab__name {
    position: absolute;
    left: 12px;
    top: 8px;
    font-size: 34px;
    line-height: 1;
    white-space: nowrap;
  }
  .name-tab__title {
    position: absolute;
    right: 13px;
    top: 43px;
    font-size: 15px;
    line-height: 1;
    white-space: nowrap;
  }

  .contact {
    position: absolute;
    left: 294px;
    top: 100px;
    font-size: 14px;
    line-height: 17px;
    color: var(--ink);
    white-space: nowrap;
  }
  .card--ice .contact { color: var(--alert); }

  .brand {
    position: absolute;
    right: 19px;
    top: 228px;
    text-align: right;
    color: var(--ink);
  }
  .brand__name {
    display: block;
    font-size: 62px;
    font-weight: 700;
    line-height: 1;
    letter-spacing: -2px;
  }
  .brand__tagline {
    display: block;
    font-size: 12px;
    line-height: 1;
    letter-spacing: 0.5px;
    margin-top: 2px;
  }
</style>
</head>
<body>
<main class="sheet">

  <section class="card card--graphite">
    <div class="name-tab">
      <span class="name-tab__name">Abcdef Ghijaklm</span>
      <span class="name-tab__title">jhkljh jgjhdhkjfytd</span>
    </div>
    <p class="contact">Phone No: 555-0147-28390<br>Email: info@dulvarosys.com</p>
    <div class="brand"><span class="brand__name">dulvaro</span><span class="brand__tagline">Systems, Inc.</span></div>
  </section>

  <section class="card card--ice">
    <div class="name-tab">
      <span class="name-tab__name">Abcdef Ghijaklm</span>
      <span class="name-tab__title">jhkljh jgjhdhkjfytd</span>
    </div>
    <p class="contact">Phone No: 555-0147-28390<br>Email: info@dulvarosys.com</p>
    <div class="brand"><span class="brand__name">dulvaro</span><span class="brand__tagline">Systems, Inc.</span></div>
  </section>

  <section class="card card--aqua">
    <div class="name-tab">
      <span class="name-tab__name">Abcdef Ghijaklm</span>
      <span class="name-tab__title">jhkljh jgjhdhkjfytd</span>
    </div>
    <p class="contact">Phone No: 555-0147-28390<br>Email: info@dulvarosys.com</p>
    <div class="brand"><span class="brand__name">dulvaro</span><span class="brand__tagline">Systems, Inc.</span></div>
  </section>

  <section class="card card--lime">
    <div class="name-tab">
      <span class="name-tab__name">Abcdef Ghijaklm</span>
      <span class="name-tab__title">jhkljh jgjhdhkjfytd</span>
    </div>
    <p class="contact">Phone No: 555-0147-28390<br>Email: info@dulvarosys.com</p>
    <div class="brand"><span class="brand__name">dulvaro</span><span class="brand__tagline">Systems, Inc.</span></div>
  </section>

</main>
</body>
</html>
```